Business Cards for Harbourline Coatings Pty Ltd

Hi every one i need a design for my buisness cards. I Want my logo in it and the name of the company needs to stand out Harbourline Coatings Pty Ltd. I want the background of the buisness cards black and i want the font to stand out in either a white or a silver stylish text. I want the design to be simple but original not to in your face if you know what i mean. I want on the back of the buisness cards to have the services that my buisness offers.
• Interior/Exterior
• Residential/Commercial
• Special effects/Texture Coatings
• Water Damage Repair
• Fully qualified
• Pensioner Discount
• 10 Year guarantee
• Fully Insured
• Obligation free quotes
full internal repaints include a proffesionla cleaning service
I want the services on the back to be layed out in an originall way not just dot points. If possible could my logo take up the whole back ground of the back but the text with the services be kind of like transparent so u cvan still see the logo i dont know if its possible it woiuld just look cool if possible. When i pick a design ill give my contact details to the designer to add to the design at the end. Any questions please just ask! Ill upload my logo.
Conatcs will include office phone: Mobile: E-mail - dale@harbourlinecoatings.com.au, Ill also have a Postal address which is a PO Box and my website is www.harbourlinecoatings.com.au

```html
<!DOCTYPE html>
<html lang="en">
<head>
<meta charset="utf-8">
<title>Harbourline Coatings Pty Ltd – Business Cards</title>
<link rel="stylesheet" href="https://fonts.googleapis.com/css2?family=Arimo:wght@400;700&family=Cormorant+Garamond:wght@500&display=swap">
<style>
  :root {
    --page-bg: #ffffff;
    --label-ink: #1a1a1a;
    --card-black: #000000;
    --card-green: #9acd47;
    --brand-green: #8dc63f;
    --ink-white: #ffffff;
    --ink-silver: #d9d9d9;
    --ink-dark: #1b1b1b;
    --watermark: rgba(255,255,255,0.12);
  }
  * { margin: 0; padding: 0; box-sizing: border-box; }
  html, body {
    width: 1200px; height: 831px; overflow: hidden;
    background: var(--page-bg);
  }
  .stage {
    position: relative;
    width: 650px; height: 450px;
    transform: scale(1.8462);
    transform-origin: 0 0;
    font-family: "Arimo", Arial, sans-serif;
  }
  .side-label {
    position: absolute;
    font-family: "Cormorant Garamond", Georgia, serif;
    font-weight: 500;
    font-size: 21px;
    letter-spacing: 0.5px;
    color: var(--label-ink);
  }
  .side-label--front { left: 16px; top: 111px; }
  .side-label--back { left: 330px; top: 115px; }

  .card {
    position: absolute;
    top: 152px;
    width: 313px; height: 192px;
    border-radius: 14px;
    overflow: hidden;
  }
  .card--front { left: 8px; background: var(--card-black); text-align: center; }
  .card--back { left: 330px; background: var(--card-green); }

  .brand-square {
    position: absolute;
    left: 133px; top: 22px;
    width: 54px; height: 54px;
    background: var(--brand-green);
    border-radius: 3px;
  }
  .company-name {
    position: absolute; left: 0; right: 0; top: 86px;
    font-weight: 700; font-size: 13.5px;
    color: var(--ink-silver);
    letter-spacing: 0.2px;
  }
  .company-suffix {
    position: absolute; left: 0; right: 0; top: 106px;
    font-weight: 700; font-size: 9px;
    color: var(--brand-green);
  }
  .contact-name {
    position: absolute; left: 0; right: 0; top: 132px;
    font-weight: 700; font-size: 14px;
    color: var(--ink-white);
  }
  .contact-line {
    position: absolute; left: 0; right: 0;
    font-size: 11px; color: var(--ink-white);
  }
  .contact-phone { top: 149px; }
  .contact-email { top: 165px; font-size: 9.5px; }

  .watermark {
    position: absolute; left: 10px; top: -20px;
    width: 230px; height: 230px;
  }
  .services {
    position: absolute; top: 19px;
    list-style: none;
    font-size: 8.6px; line-height: 12.3px;
    color: var(--ink-dark);
  }
  .services--left { left: 13px; width: 140px; }
  .services--right { left: 158px; width: 150px; }
  .service { position: relative; padding-left: 9px; }
  .service::before {
    content: "✓"; position: absolute; left: 0; top: 0;
    font-size: 8px;
  }
  .service--strong { font-weight: 700; }
  .service--note { line-height: 10.5px; padding-top: 1px; }

  .back-company {
    position: absolute; left: 24px; top: 143px;
    font-size: 8.2px; font-weight: 700; color: var(--ink-dark);
  }
  .back-address {
    position: absolute; left: 24px; top: 153px;
    font-size: 7px; color: var(--ink-dark);
  }
  .back-web {
    position: absolute; left: 24px; top: 167px;
    font-size: 9.2px; font-weight: 700; color: var(--ink-dark);
  }
</style>
</head>
<body>
<main class="stage">
  <p class="side-label side-label--front">FRONT</p>
  <p class="side-label side-label--back">BACK</p>

  <section class="card card--front" aria-label="Business card front">
    <div class="brand-square" aria-hidden="true"></div>
    <p class="company-name">HARBOURLINE COATINGS</p>
    <p class="company-suffix">PTY LTD</p>
    <p class="contact-name">Dale Whitmore</p>
    <p class="contact-line contact-phone">+65 80457319</p>
    <p class="contact-line contact-email">dale@harbourlinecoatings.com.au</p>
  </section>

  <section class="card card--back" aria-label="Business card back">
    <svg class="watermark" viewBox="0 0 230 230" aria-hidden="true">
      <circle cx="115" cy="115" r="108" fill="none" stroke="var(--watermark)" stroke-width="14"/>
    </svg>
    <ul class="services services--left">
      <li class="service">Interior/Exterior</li>
      <li class="service service--strong">Residential/Commercial</li>
      <li class="service">Special efforts/Texture coatings</li>
      <li class="service service--strong">Water damage repair</li>
      <li class="service">Fully qualified</li>
      <li class="service service--strong">Pensioner Discount</li>
    </ul>
    <ul class="services services--right">
      <li class="service">10 Year gurantee</li>
      <li class="service service--strong">Fully insured</li>
      <li class="service">Obligation free quotes</li>
      <li class="service service--strong service--note">Full internal repaints inculde a proffesionla cleaning services</li>
    </ul>
    <p class="back-company">HARBOURLINE COATINGS PTY LTD</p>
    <p class="back-address">428 Ferrow Ave., Kelmont, CA 93104</p>
    <p class="back-web">www.harbourlinecoatings.com.au</p>
  </section>
</main>
</body>
</html>
```